"Thank You" flyer design

We need a "thank you" flyer that will be sent out with all our products.
a6 size landscape,
We manufacture personalised shaped signs.
I've attached a rough idea of what we are after, but would like it to be improved upon with some artistic flare..

Side one - We would like the flyer to have a simple message - "thank you for shopping with us"

Side two - we would also like our logo and a union jack made in the UK badge and our address and contact details with our website www.lumkinprints.co.uk being the most prominent..

We are after a simple bold design what would be printed on a small a6 card that people might hopefully want to keep, so the end design needs to be pretty cool.

Industry/Entity Type

Shopping

Font styles to use
Serif
Sans Serif

```html
<!DOCTYPE html>
<html lang="en">
<head>
<meta charset="utf-8">
<title>Thank You for Shopping with Us</title>
<link href="https://fonts.googleapis.com/css2?family=Alfa+Slab+One&display=swap" rel="stylesheet">
<style>
  :root {
    --sky: #29a6df;
    --sky-band: #8ad2f1;
    --ribbon: #9fdaf4;
    --white: #ffffff;
    --magenta: #e4187d;
    --screw: #6dbfe6;
  }
  html, body {
    margin: 0;
    padding: 0;
    overflow: hidden;
    background: var(--sky);
  }
  .flyer {
    position: relative;
    width: 1200px;
    height: 861px;
    overflow: hidden;
    background: var(--sky);
  }
  .flyer-art {
    position: absolute;
    inset: 0;
  }
  .outline-pattern {
    position: absolute;
    inset: 0;
    background: radial-gradient(ellipse at 35% 55%, rgba(255,255,255,0.10), rgba(255,255,255,0) 70%);
  }
  .headline {
    position: absolute;
    left: 0;
    top: 0;
    margin: 0;
    font-family: "Alfa Slab One", serif;
    font-weight: 400;
    color: var(--magenta);
  }
  .headline-thanks {
    position: absolute;
    left: 178px;
    top: 122px;
    font-size: 150px;
    line-height: 1;
    letter-spacing: -1px;
    white-space: nowrap;
  }
  .headline-for {
    position: absolute;
    left: 592px;
    top: 252px;
    font-size: 30px;
    line-height: 1;
  }
  .headline-shopping {
    position: absolute;
    left: 172px;
    top: 283px;
    font-size: 80px;
    line-height: 1;
    white-space: nowrap;
    letter-spacing: -0.5px;
  }
  .web-address {
    position: absolute;
    left: 600px;
    top: 755px;
    margin: 0;
    font-family: "Alfa Slab One", serif;
    font-size: 58px;
    line-height: 1;
    color: var(--magenta);
    transform: rotate(-8deg);
    transform-origin: left bottom;
    white-space: nowrap;
  }
</style>
</head>
<body>
  <main class="flyer">
    <div class="outline-pattern" role="img" aria-label="Faint outline pattern of assorted sign shapes across the background"></div>

    <svg class="flyer-art" width="1200" height="861" viewBox="0 0 1200 861" aria-hidden="true">
      <rect class="ribbon-band" x="0" y="208" width="1200" height="153" fill="var(--sky-band)"/>

      <polygon class="ribbon" points="70,105 1125,105 1005,258 1125,411 70,411 190,258"
               fill="var(--ribbon)" stroke="var(--white)" stroke-width="5"/>
      <polygon class="ribbon-inner-line" points="92,118 1103,118 990,258 1103,398 92,398 205,258"
               fill="none" stroke="var(--white)" stroke-width="2.5"/>

      <g class="ribbon-screws" fill="var(--white)" stroke="var(--screw)" stroke-width="2">
        <circle cx="125" cy="139" r="10"/>
        <circle cx="125" cy="378" r="10"/>
        <circle cx="1070" cy="139" r="10"/>
        <circle cx="1070" cy="378" r="10"/>
        <line x1="118" y1="146" x2="132" y2="132"/>
        <line x1="118" y1="385" x2="132" y2="371"/>
        <line x1="1063" y1="146" x2="1077" y2="132"/>
        <line x1="1063" y1="385" x2="1077" y2="371"/>
      </g>

      <polygon class="corner-band-light" points="0,861 0,822 1200,650 1200,861" fill="var(--sky-band)"/>
      <line class="corner-stripe" x1="0" y1="800" x2="1200" y2="628" stroke="var(--white)" stroke-width="4"/>
      <polygon class="corner-band-white" points="470,861 1200,690 1200,861" fill="var(--white)"/>
    </svg>

    <h1 class="headline">
      <span class="headline-thanks">Thank You</span>
      <span class="headline-for">for</span>
      <span class="headline-shopping">Shopping with us</span>
    </h1>

    <p class="web-address">lumkinprints.co.uk</p>
  </main>
</body>
</html>
```